Fiber To The Home

We want a 6x9 add front and back I like the ads I saw for Tavlin. I want something that will stand out (Funny) but looks professional.

Target Market(s)

Residential

Requirements
Must have
• I'm not sure what I want. Our prices are on our website. I really like a few adds that I saw on here Tavlin

```html
<!DOCTYPE html>
<html lang="en">
<head>
<meta charset="utf-8">
<title>Solstra — Postcard</title>
<link rel="stylesheet" href="https://fonts.googleapis.com/css2?family=Montserrat:wght@400;500;600;700;800&display=swap">
<style>
  :root{
    --navy:#14307f;
    --royal:#1f47a8;
    --deep:#0c1f5c;
    --cyan:#29b3e8;
    --ink:#1b2a5a;
    --paper:#ffffff;
    --stage:#eeeeee;
    --rule:#9aa3b5;
  }
  *{box-sizing:border-box;margin:0;padding:0}
  html,body{width:689px;height:1200px;overflow:hidden;background:var(--stage)}
  body{position:relative;font-family:"Montserrat",sans-serif;color:var(--ink)}
  .card{position:absolute;left:44px;width:600px;height:400px;overflow:hidden;background:var(--paper);box-shadow:0 4px 14px rgba(0,0,0,.18)}
  .card--front{top:140px}
  .card--back{top:660px}

  /* front */
  .hero-art{position:absolute;inset:0 0 80px 0;background:radial-gradient(ellipse at 55% 95%,#d9e7f7 0%,#7fa6dc 22%,#2f5fb4 48%,#10296f 78%,#081746 100%)}
  .brand-front{position:absolute;top:22px;left:0;right:0;text-align:center;color:#fff;font-weight:700;font-size:42px;letter-spacing:1px;line-height:1}
  .tagline-band{position:absolute;left:0;right:0;bottom:0;height:80px;background:linear-gradient(180deg,var(--royal),var(--navy));border-top:2px solid #c9d4ea;color:#fff;text-align:center;padding-top:14px}
  .tagline{font-size:25px;font-weight:400;letter-spacing:.3px;line-height:1}
  .tagline b{font-weight:700}
  .tagline-sub{font-size:8.6px;margin-top:8px;line-height:1.3}

  /* back */
  .back-art{position:absolute;inset:0}
  .brand-back{position:absolute;top:10px;left:0;width:320px;text-align:center;color:var(--navy);font-weight:700;font-size:22px;line-height:1;letter-spacing:.5px}
  .features{position:absolute;top:48px;left:12px;width:300px;display:flex}
  .feature{flex:1;text-align:center;border-left:1px solid #cfd5e0;padding-top:4px}
  .feature:first-child{border-left:none}
  .feature svg{width:38px;height:42px;display:block;margin:0 auto 4px}
  .feature-label{font-size:7.5px;font-weight:700;color:var(--navy)}
  .packages-title{position:absolute;top:126px;left:14px;font-size:16.5px;font-weight:400;color:var(--navy);letter-spacing:.2px}
  .packages-title b{font-weight:800}
  .packages{position:absolute;top:148px;left:15px;width:292px;display:flex;gap:2px}
  .plan{flex:1;background:rgba(255,255,255,.92);text-align:center}
  .plan-head{background:var(--deep);color:#fff;height:30px;padding-top:5px}
  .plan-speed{font-size:8.5px;font-weight:500}
  .plan-tier{font-size:6.5px;font-weight:700;color:var(--cyan)}
  .plan-price{font-size:20px;font-weight:700;color:var(--cyan);text-align:left;padding:6px 0 4px 6px;border-bottom:1px solid #d5dae4}
  .plan-price sup{font-size:8px;color:var(--ink);vertical-align:10px}
  .plan-price small{font-size:6.5px;font-weight:400;color:#555}
  .plan-note{font-size:5.6px;font-weight:600;line-height:1.35;padding:5px 4px 6px;color:#333}
  .services-title{position:absolute;top:290px;left:0;width:320px;text-align:center;font-size:17px;font-weight:800;color:var(--navy)}
  .services{position:absolute;top:313px;left:18px;width:290px;display:flex}
  .services ul{flex:1;list-style:none;font-size:7.3px;line-height:1.9;color:#333}
  .services ul + ul{border-left:1px solid #bfc6d4;padding-left:8px}
  .services li::before{content:"•";margin-right:5px}
  .contact-bar{position:absolute;left:0;bottom:0;width:330px;height:28px;background:var(--navy);color:#fff;display:flex;align-items:center;padding-left:16px;gap:9px;font-size:14px;font-weight:500}
  .contact-bar .web{font-size:12px;border-left:1px solid #fff;padding-left:9px;display:flex;align-items:center;gap:5px}
  .contact-bar svg{width:14px;height:14px}
  .chevron{position:absolute;inset:0;pointer-events:none}
  .stamp-box{position:absolute;top:20px;right:18px;width:76px;height:70px;border:1px solid #9a9a9a}
  .address-line{position:absolute;right:18px;width:188px;border-top:1px solid var(--rule)}
</style>
</head>
<body>

<section class="card card--front">
  <div class="hero-art" role="img" aria-label="Photo of a night sky with a crescent moon and a businessman riding a rocket through the clouds"></div>
  <div class="brand-front">Solstra</div>
  <div class="tagline-band">
    <div class="tagline">YOUR <b>SUCCESS</b> IS OUR <b>BUSINESS</b></div>
    <div class="tagline-sub">Serving local residents and businesses for more than 15 years. Providing internet &amp; satellite services<br>to residential homes, commercial businesses, and multi-dwelling unit properties.</div>
  </div>
</section>

<section class="card card--back">
  <svg class="back-art" viewBox="0 0 600 400" preserveAspectRatio="none">
    <defs>
      <linearGradient id="backPhoto" x1="0" y1="0" x2="1" y2="1">
        <stop offset="0" stop-color="#f4f2ef"/>
        <stop offset=".5" stop-color="#e4e3e4"/>
        <stop offset="1" stop-color="#cfd4dc"/>
      </linearGradient>
    </defs>
    <path role="img" aria-label="Soft photo of a person working on a laptop" d="M0 0H305L362 205L305 400H0Z" fill="url(#backPhoto)"/>
  </svg>

  <div class="brand-back">Solstra</div>

  <div class="features">
    <div class="feature">
      <svg viewBox="0 0 38 42"><path d="M19 1L37 11V31L19 41L1 31V11Z" fill="var(--royal)"/><rect x="10" y="16" width="18" height="13" rx="1.5" fill="#fff"/><path d="M15 16v-3h8v3" fill="none" stroke="#fff" stroke-width="2"/><path d="M10 21h18" stroke="var(--royal)" stroke-width="1.2"/></svg>
      <div class="feature-label">BUSINESS SOLUTIONS</div>
    </div>
    <div class="feature">
      <svg viewBox="0 0 38 42"><path d="M19 1L37 11V31L19 41L1 31V11Z" fill="var(--royal)"/><path d="M9 21L19 12L29 21H26V30H12V21Z" fill="#fff"/><rect x="17" y="24" width="4" height="6" fill="var(--royal)"/></svg>
      <div class="feature-label">HOME SOLUTIONS</div>
    </div>
    <div class="feature">
      <svg viewBox="0 0 38 42"><path d="M19 1L37 11V31L19 41L1 31V11Z" fill="var(--royal)"/><g fill="none" stroke="#fff" stroke-width="1.6"><circle cx="19" cy="21" r="9"/><ellipse cx="19" cy="21" rx="4" ry="9"/><path d="M10 21h18M12 16h14M12 26h14"/></g></svg>
      <div class="feature-label">UNLIMITED INTERNET</div>
    </div>
  </div>

  <div class="packages-title"><b>RESIDENTIAL</b> INTERNET PACKAGES</div>

  <div class="packages">
    <div class="plan">
      <div class="plan-head"><div class="plan-speed">15/15 MBPS</div><div class="plan-tier">BASIC</div></div>
      <div class="plan-price"><sup>$</sup>35<small>/Month</small></div>
      <div class="plan-note">UNLIMITED! No Data Caps! Web Browsing, Social Media, Email. Great for Single-User Households.</div>
    </div>
    <div class="plan">
      <div class="plan-head"><div class="plan-speed">30/30 MBPS</div><div class="plan-tier">CHOICE</div></div>
      <div class="plan-price"><sup>$</sup>45<small>/Month</small></div>
      <div class="plan-note">UNLIMITED! No Data Caps! HD Streaming, Online Gaming. Great for Multi-User Households.</div>
    </div>
    <div class="plan">
      <div class="plan-head"><div class="plan-speed">100/100 MBPS</div><div class="plan-tier">PERFORMANCE</div></div>
      <div class="plan-price"><sup>$</sup>65<small>/Month</small></div>
      <div class="plan-note">UNLIMITED! No Data Caps! HD Streaming, Online Gaming. Great for Multi-User Households.</div>
    </div>
    <div class="plan">
      <div class="plan-head"><div class="plan-speed">150/150 MBPS</div><div class="plan-tier">CHOICE</div></div>
      <div class="plan-price"><sup>$</sup>85<small>/Month</small></div>
      <div class="plan-note">UNLIMITED! No Data Caps! 4K Streaming, Online Gaming. Great for Multi-User Households.</div>
    </div>
  </div>

  <div class="services-title">SERVICES</div>
  <div class="services">
    <ul>
      <li>Experienced Service Technicians</li>
      <li>Custom Business Solutions</li>
      <li>Latest In Technology</li>
    </ul>
    <ul>
      <li>Exceptional Customer Service</li>
      <li>No Long Term Contract</li>
      <li>Plans That Fit Every Budget</li>
    </ul>
  </div>

  <div class="contact-bar">
    <svg viewBox="0 0 14 14"><circle cx="7" cy="7" r="6.3" fill="none" stroke="#fff" stroke-width="1.2"/><path d="M4.6 3.8l1.3-.3.7 1.7-.8.6c.4.9 1 1.5 1.9 1.9l.6-.8 1.7.7-.3 1.3c-2.8.1-5.2-2.3-5.1-5.1z" fill="#fff"/></svg>
    <span>+1 555-014-2290</span>
    <span class="web"><svg viewBox="0 0 14 14"><circle cx="7" cy="7" r="6.3" fill="none" stroke="#fff" stroke-width="1.2"/><ellipse cx="7" cy="7" rx="2.6" ry="6.3" fill="none" stroke="#fff" stroke-width="1"/><path d="M.7 7h12.6" stroke="#fff" stroke-width="1"/></svg>solstrasatellite.tv</span>
  </div>

  <svg class="chevron" viewBox="0 0 600 400" preserveAspectRatio="none">
    <path d="M290 0H300L357 205L300 400H290L347 205Z" fill="#8ea8d8"/>
    <path d="M305 0H335L392 205L335 400H305L362 205Z" fill="var(--navy)"/>
  </svg>

  <div class="stamp-box"></div>
  <div class="address-line" style="top:255px"></div>
  <div class="address-line" style="top:300px"></div>
  <div class="address-line" style="top:344px"></div>
</section>

</body>
</html>
```